A Maple Syrup Label for a Local Buniness

We are looking for a label for our maple syrup business. Our business currently sells honey, and we are expanding into maple syrup. Our Business name is "Corvale Bees" and we currently have a logo attached below. We would like to incorporate the bee and CB part, but the label could also read "Corvale Farms" with the words maple syrup. We do not want consumers to confuse the maple syrup jars with the honey jars. It should be clear that the jars contain maple syrup. We are open to new designs as well.

```html
<!DOCTYPE html>
<html lang="en">
<head>
<meta charset="utf-8">
<title>Corvale Farms Maple Syrup Label</title>
<link href="https://fonts.googleapis.com/css2?family=Cinzel:wght@400;600&display=swap" rel="stylesheet">
<style>
  :root {
    --page: #ffffff;
    --maple-red: #9c2721;
    --maple-red-soft: #a8342a;
    --leaf-white: #ffffff;
    --ink: #111111;
    --farms-red: #9a2b22;
    --pill-border: #a0521c;
    --pill-text: #ffffff;
  }
  * { margin: 0; padding: 0; box-sizing: border-box; }
  html, body {
    width: 1200px;
    height: 651px;
    overflow: hidden;
    background: var(--page);
  }
  .label {
    position: absolute;
    left: 112px;
    top: 25px;
    width: 976px;
    height: 600px;
    overflow: hidden;
    background: radial-gradient(ellipse at center, var(--maple-red-soft) 0%, var(--maple-red) 70%);
    box-shadow: 4px 6px 10px rgba(0,0,0,0.25);
    font-family: "Cinzel", "Times New Roman", serif;
  }
  .leaf-area {
    position: absolute;
    left: 0;
    top: 0;
    width: 976px;
    height: 600px;
  }
  .brand-mark {
    position: absolute;
    left: 0;
    width: 100%;
    top: 138px;
    display: flex;
    justify-content: center;
    align-items: center;
    gap: 10px;
    font-size: 30px;
    font-weight: 600;
    color: var(--ink);
    line-height: 1;
  }
  .brand-mark .dot {
    width: 16px;
    height: 16px;
    border-radius: 50%;
    background: var(--ink);
  }
  .wordmark {
    position: absolute;
    left: 0;
    width: 100%;
    text-align: center;
    line-height: 1;
    font-weight: 400;
  }
  .wordmark--top {
    top: 237px;
    font-size: 84px;
    color: var(--ink);
  }
  .wordmark--bottom {
    top: 312px;
    font-size: 84px;
    color: var(--farms-red);
    letter-spacing: 2px;
  }
  .volume {
    position: absolute;
    left: 0;
    width: 100%;
    top: 402px;
    text-align: center;
    font-size: 24px;
    line-height: 1;
    color: var(--ink);
  }
  .product-pill {
    position: absolute;
    left: 279px;
    top: 495px;
    width: 416px;
    height: 51px;
    border-radius: 26px;
    background: var(--ink);
    border: 3px solid var(--pill-border);
    display: flex;
    align-items: center;
    justify-content: center;
    color: var(--pill-text);
    font-size: 36px;
    line-height: 1;
    letter-spacing: 1px;
  }
</style>
</head>
<body>
  <main class="label">
    <svg class="leaf-area" viewBox="0 0 976 600" role="img" aria-label="Large white maple leaf silhouette over a pattern of outlined maple leaves">
      <ellipse cx="488" cy="270" rx="360" ry="262" fill="var(--leaf-white)"/>
    </svg>
    <div class="brand-mark"><span class="dot"></span><span>Corvale Bees</span></div>
    <h1 class="wordmark wordmark--top">CORVALE</h1>
    <h2 class="wordmark wordmark--bottom">FARMS</h2>
    <p class="volume">500ML</p>
    <p class="product-pill">MAPLE SYRUP</p>
  </main>
</body>
</html>
```